Builders Worksite Corflute Outdoor Sign

We are a building company who are just branching out into new construction. How first new build is our own home which was designed by us and a local architect. We are proud and want to create more advertisement around our business.

We need a corflute sign that can staked outside the construction site and can be seen by people passing by.
Updates

Can we please make the company name and logo bigger (Tidewater Lane Homes) This needs to be the focus. Can we please replace 'Mako' with 'Contact Us on 021-649-3157'

Target Market(s)

Home owners and people wishing to build on lifestyle blocks in New Zealand.

Font styles to use
Sans Serif

Requirements
Must have
• It needs to feature our:
Logo
Company name
Contact name and number - Mako - 0216493157
Landscape NOT portrait.

```html
<!DOCTYPE html>
<html lang="en">
<head>
<meta charset="utf-8">
<title>Tidewater Lane Homes – Site Sign</title>
<link rel="stylesheet" href="https://fonts.googleapis.com/css2?family=Jost:wght@400;500;700&display=swap">
<style>
  :root {
    --navy: #15213a;
    --gold: #f0bd1a;
    --gold-deep: #d9a314;
    --paper: #f7f7f7;
    --white: #ffffff;
  }
  html, body {
    margin: 0;
    padding: 0;
    width: 1200px;
    height: 919px;
    overflow: hidden;
    background: var(--paper);
  }
  .sign {
    position: relative;
    width: 1200px;
    height: 919px;
    overflow: hidden;
    background: var(--paper);
    font-family: "Jost", "Futura", sans-serif;
    color: var(--navy);
  }
  .sign__shapes {
    position: absolute;
    inset: 0;
  }
  .brand__dot {
    position: absolute;
    left: 558px;
    top: 165px;
    width: 84px;
    height: 84px;
    border-radius: 50%;
    background: var(--gold);
  }
  .brand__name {
    position: absolute;
    left: 0;
    right: 0;
    top: 300px;
    margin: 0;
    text-align: center;
    font-weight: 400;
    font-size: 112px;
    line-height: 1;
    letter-spacing: 0.01em;
    color: var(--navy);
    white-space: nowrap;
  }
  .brand__name-sub {
    display: block;
    margin-top: 40px;
    font-size: 92px;
    letter-spacing: 0.42em;
    padding-left: 0.42em;
  }
  .contact {
    position: absolute;
    left: 0;
    right: 0;
    top: 750px;
    text-align: center;
  }
  .contact__label {
    display: inline-flex;
    align-items: center;
    gap: 16px;
    font-size: 40px;
    font-weight: 500;
    line-height: 1;
  }
  .contact__label::before,
  .contact__label::after {
    content: "";
    width: 128px;
    height: 2px;
    background: var(--navy);
  }
  .contact__phone {
    display: flex;
    justify-content: center;
    align-items: center;
    gap: 14px;
    margin-top: 22px;
    font-size: 66px;
    font-weight: 700;
    line-height: 1;
    letter-spacing: 0.01em;
  }
  .contact__icon {
    width: 56px;
    height: 56px;
  }
</style>
</head>
<body>
<main class="sign">
  <svg class="sign__shapes" width="1200" height="919" viewBox="0 0 1200 919" aria-hidden="true">
    <polygon class="band-gold" points="0,794 254,621 644,736 1085,613 1200,589 1200,919 0,919" fill="var(--gold)"/>
    <polygon class="corner-navy-left" points="0,629 198,684 0,794" fill="var(--navy)"/>
    <polygon class="corner-navy-right" points="1200,589 1200,804 921,678" fill="var(--navy)"/>
    <line class="accent-line" x1="254" y1="632" x2="547" y2="717" stroke="var(--navy)" stroke-width="5"/>
    <line class="accent-line" x1="849" y1="696" x2="1140" y2="615" stroke="var(--white)" stroke-width="5"/>
    <polygon class="arrow-white" points="162,720 233,682 233,742" fill="var(--white)"/>
    <polygon class="arrow-white" points="1099,776 1183,815 1099,856" fill="var(--white)"/>
  </svg>

  <div class="brand__dot"></div>
  <h1 class="brand__name">TIDEWATER LANE<span class="brand__name-sub">HOMES</span></h1>

  <section class="contact">
    <div class="contact__label">Contact Us</div>
    <div class="contact__phone">
      <svg class="contact__icon" viewBox="0 0 56 56" aria-hidden="true">
        <circle cx="28" cy="28" r="26" fill="none" stroke="var(--white)" stroke-width="2"/>
        <circle cx="28" cy="28" r="22" fill="var(--gold-deep)"/>
        <path d="M20 17c1.5-1 3-0.6 3.8 0.8l2 3.6c0.7 1.3 0.3 2.6-0.8 3.4l-1.3 1c1.2 2.8 3.2 4.8 6 6l1-1.3c0.8-1.1 2.1-1.5 3.4-0.8l3.6 2c1.4 0.8 1.8 2.3 0.8 3.8l-1.3 1.8c-1.2 1.6-3.3 2.2-5.2 1.5C24.6 36.5 19.5 31.4 17.2 24.2c-0.7-1.9-0.1-4 1.5-5.2z" fill="var(--navy)"/>
        <path d="M31 17a9 9 0 0 1 8 8M31 12a14 14 0 0 1 13 13" fill="none" stroke="var(--navy)" stroke-width="2.2" stroke-linecap="round"/>
      </svg>
      <span class="contact__number">021-649-3157</span>
    </div>
  </section>
</main>
</body>
</html>
```